Marcus Lindqvist Photography needs a business card designs

I am looking for a business card with a logo clean and simple which I can use that logo on my website or on my pictures. It has to be very classy and very professional. Please look at my website at www.marcuslvqphoto.com for my signature. I'm thinking of something like that for my signature/logo. I'm still working on my website but you get an idea. I'm open to any design but not too busy graphics.

I will be printing the business card from qrivel.com.

Surprise me :)

contact me if you have any questions.

-ML

I'm receiving a lot of black background at the moment. I know my website is all black doesn't mean I want my card to be all black. Please send in with some white background as well. Thanks :)

check out some business cards that I found online. I think they are simple and look really awesome. I don't want a card that is too busy.

http://www.marcuslvqphoto.com/p270092084

Reason: Please extend the date for me. I haven't really receive any good design yet.

Printing

• -a logo that related to my first and last initial of my name "ML"
-double sided
• -I don't want my background to be all black.
-no pictures on the card

```html
<!DOCTYPE html>
<html lang="en">
<head>
<meta charset="utf-8">
<title>Marcus Lindqvist Photography — Business Card</title>
<link rel="stylesheet" href="https://fonts.googleapis.com/css2?family=Cinzel:wght@700&family=Tinos&display=swap">
<style>
  :root {
    --backdrop: #8e8e8e;
    --card-dark: #000000;
    --card-light: #ffffff;
    --ink-light: #ffffff;
    --ink-dark: #111111;
    --ink-muted: #555555;
    --mark-faint: #e6e6e6;
    --name-font: "Cinzel", Georgia, serif;
    --body-font: "Tinos", "Times New Roman", serif;
  }
  * { box-sizing: border-box; margin: 0; padding: 0; }
  html, body { width: 927px; height: 1200px; overflow: hidden; }
  body {
    background: var(--backdrop);
    display: flex;
    flex-direction: column;
    align-items: center;
    justify-content: center;
    gap: 110px;
  }
  .card {
    position: relative;
    width: 700px;
    height: 350px;
    box-shadow: 0 6px 18px rgba(0,0,0,0.35);
  }
  .card::after {
    content: "";
    position: absolute;
    inset: 9px;
    pointer-events: none;
  }

  /* Front */
  .card--front { background: var(--card-dark); color: var(--ink-light); }
  .card--front::after { border: 2px solid var(--ink-light); }
  .card--front .brand {
    position: absolute;
    inset: 0;
    display: flex;
    flex-direction: column;
    align-items: center;
    justify-content: center;
  }
  .brand__dot {
    width: 88px;
    height: 88px;
    border-radius: 50%;
    border: 3px solid var(--ink-light);
    margin-bottom: 22px;
  }
  .brand__name {
    font-family: var(--name-font);
    font-weight: 700;
    font-size: 50px;
    line-height: 1;
    letter-spacing: 0.01em;
  }
  .brand__tagline {
    font-family: var(--name-font);
    font-weight: 700;
    font-size: 15px;
    letter-spacing: 1.05em;
    margin-top: 12px;
    margin-right: -1.05em;
  }

  /* Back */
  .card--back { background: var(--card-light); color: var(--ink-dark); }
  .card--back::after { border: 2px solid var(--ink-dark); }
  .card__watermark {
    position: absolute;
    left: 50%;
    top: 50%;
    width: 270px;
    height: 270px;
    transform: translate(-38%, -50%);
    border-radius: 50%;
    background: var(--mark-faint);
    opacity: 0.7;
  }
  .contact {
    position: absolute;
    left: 225px;
    top: 108px;
  }
  .contact__name {
    font-family: var(--name-font);
    font-weight: 700;
    font-size: 28px;
    line-height: 1;
  }
  .contact__tagline {
    font-family: var(--name-font);
    font-weight: 700;
    font-size: 10px;
    letter-spacing: 0.95em;
    color: var(--ink-dark);
    margin: 6px 0 8px;
  }
  .contact__list { list-style: none; font-family: var(--body-font); font-size: 15px; line-height: 1.3; }
</style>
</head>
<body>
  <section class="card card--front" aria-label="Card front">
    <div class="brand">
      <div class="brand__dot"></div>
      <h1 class="brand__name">Marcus Lindqvist</h1>
      <p class="brand__tagline">PHOTOGRAPHY</p>
    </div>
  </section>

  <section class="card card--back" aria-label="Card back">
    <div class="card__watermark" role="img" aria-label="Faint brand circle"></div>
    <div class="contact">
      <h2 class="contact__name">Marcus Lindqvist</h2>
      <p class="contact__tagline">PHOTOGRAPHY</p>
      <ul class="contact__list">
        <li>Contact number:</li>
        <li>email address:</li>
        <li>&nbsp;Website:</li>
      </ul>
    </div>
  </section>
</body>
</html>
```